Can you make our site AWESOME?

Hi Guys,

I am a co-founder of Tumble Crate Rentals Oz, the world's first e-commerce skip bin business.

We are looking to update our site before a launch into the UK in March.

Please help us by submitting your designs for the following pages:

- Home page (www.tumblecraterentalsoz.example.au)
- About us (https://www.tumblecraterentalsoz.example.au/pages/about-us
- Contact us (https://www.tumblecraterentalsoz.example.au/pages/contact-us)
- Quick Quote / Pricing (https://www.tumblecraterentalsoz.example.au/pages/free-instant-quote-skip-bin-hire)

NOTES:
- Design should be high-converting
- best designs will be fresh, modern, easy to read, distinctive and memorable
- please use our logo and video colours
- feel free to change logos, layout, images and anything else you feel can be improved
- the winning designer will potentially have the opportunity to re-design the other pages on our site
- brief is for design only

Any questions just ask.

Thanks,
Morton

```html
<!DOCTYPE html>
<html lang="en">
<head>
<meta charset="utf-8">
<title>Tumble Crate Rentals Oz – Home</title>
<link href="https://fonts.googleapis.com/css2?family=Open+Sans:wght@300;400;600;700&display=swap" rel="stylesheet">
<style>
:root{
  --navy:#111a3d;
  --navy-soft:#2a3566;
  --green:#2f7d34;
  --green-dark:#1f5e25;
  --green-light:#3e9a44;
  --orange:#e9472a;
  --purple:#6d70b8;
  --sky:#cfe8f7;
  --sky-deep:#8cc6ea;
  --grey:#ededed;
  --text:#333;
  --muted:#666;
  --white:#fff;
}
*{box-sizing:border-box;margin:0;padding:0}
html,body{width:1200px;height:5294px;overflow:hidden}
body{font-family:"Open Sans",Arial,sans-serif;color:var(--text);background:var(--white);position:relative}
a{color:inherit;text-decoration:none}
.abs{position:absolute}

/* top bar */
.topbar{position:absolute;top:0;left:0;width:1200px;height:42px;background:var(--navy);color:#fff;font-size:14px;display:flex;align-items:center;justify-content:space-between;padding:0 88px}
.topbar .right{display:flex;gap:28px;align-items:center}
/* nav */
.nav{position:absolute;top:42px;left:0;width:1200px;height:134px;background:#fff;display:flex;align-items:center;justify-content:space-between;padding:0 88px}
.brand{display:flex;align-items:center;gap:12px;font-weight:700;font-size:22px;color:var(--navy);letter-spacing:.3px}
.brand .mark{width:34px;height:34px;background:var(--green);border-radius:4px}
.menu{display:flex;gap:34px;font-size:14px;color:var(--navy);font-weight:600}
.nav-rule{position:absolute;top:160px;left:88px;width:1024px;height:1px;background:#ccc}

/* hero */
.hero{position:absolute;top:176px;left:0;width:1200px;height:560px;background:linear-gradient(180deg,#e9f5fc 0%,var(--sky) 45%,var(--sky-deep) 100%)}
.hero .city{position:absolute;left:0;top:40px;width:1200px;height:420px;background:linear-gradient(180deg,rgba(255,255,255,0) 0%,rgba(140,190,225,.55) 60%,rgba(110,170,215,.7) 100%)}
.hero .wave{position:absolute;left:0;bottom:-1px}
.hero h1{position:absolute;top:70px;width:100%;text-align:center;font-size:42px;font-weight:700;color:#111}
.hero .tag{position:absolute;top:138px;width:100%;text-align:center;font-size:22px;color:#222}
.hero h2{position:absolute;top:200px;width:100%;text-align:center;font-size:27px;font-weight:600;color:#111}
.search{position:absolute;height:76px;background:#fff;border-radius:40px;box-shadow:0 4px 14px rgba(0,0,0,.15);display:flex;align-items:center;justify-content:space-between;padding:0 6px 0 28px;font-size:16px;color:#777}
.search .btn{background:var(--orange);color:#fff;font-weight:700;font-size:22px;height:64px;padding:0 32px;border-radius:34px;display:flex;align-items:center}
.hero .search{top:280px;left:280px;width:640px}
.call{position:absolute;height:44px;padding:0 30px;border-radius:24px;background:var(--purple);color:#fff;font-weight:700;font-size:21px;display:flex;align-items:center;box-shadow:0 0 0 5px rgba(109,112,184,.25)}
.hero .call{top:400px;left:530px}

.segments{position:absolute;top:672px;left:0;width:1200px;height:200px}
.seg{position:absolute;text-align:center;font-size:19px;font-weight:600;color:#222;width:160px}
.seg .c{width:110px;height:110px;border-radius:50%;background:#fff;border:2px solid #ddd;margin:0 auto 14px;display:flex;align-items:center;justify-content:center;box-shadow:0 3px 8px rgba(0,0,0,.1)}
.seg.active .c{background:var(--green);border:6px solid #cfe6d0;width:120px;height:120px}

/* about */
.section-title{position:absolute;width:1200px;text-align:center;font-weight:300;font-size:44px;color:#111}
.about-text{position:absolute;top:1030px;left:190px;width:820px;text-align:center;font-size:14px;line-height:26px;color:#444}
.grey-band{position:absolute;left:0;width:1200px;background:var(--grey)}
.video{position:absolute;top:1200px;left:141px;width:918px;height:530px;background:linear-gradient(180deg,#6b67a8 0%,#7b77b6 55%,#5c9a4e 82%,#3d7a35 100%);box-shadow:0 10px 24px rgba(0,0,0,.18)}
.video .play{position:absolute;left:430px;top:230px;width:76px;height:76px;border-radius:50%;background:#fff;border:5px solid #2a2f5c;display:flex;align-items:center;justify-content:center}

/* steps */
.step{position:absolute;top:1924px;width:290px;height:290px;border-radius:50%;background:#fff;border:10px solid var(--green);box-shadow:0 8px 18px rgba(0,0,0,.12);text-align:center;padding-top:66px}
.step.mid{background:var(--green);border-color:var(--navy);color:#fff;top:1914px;width:310px;height:310px}
.step h3{font-size:17px;font-weight:600;margin:14px 0 8px}
.step p{font-size:13px;line-height:18px;color:#555;padding:0 70px}
.step.mid p{color:#e4f2e4}

/* trade secrets */
.card{position:absolute;top:2422px;background:#fff;box-shadow:0 6px 16px rgba(0,0,0,.15)}
.card .photo{width:100%;height:272px}
.card .body{padding:18px 34px}
.card h4{font-size:21px;font-weight:400;color:#111;margin-bottom:10px}
.card p{font-size:13px;line-height:19px;color:#444}
.card .more{display:block;margin-top:14px;color:var(--orange);font-size:12px;font-weight:700}

/* savings */
.save{position:absolute;top:3007px;left:0;width:1200px;height:653px;background:linear-gradient(135deg,var(--green-light) 0%,var(--green) 45%,var(--green-dark) 100%);color:#fff}
.save h2{position:absolute;top:98px;width:100%;text-align:center;font-weight:300;font-size:42px}
.benefit{position:absolute;top:225px;width:300px;text-align:center}
.benefit .c{width:170px;height:170px;border-radius:50%;background:#fff;border:6px solid #cfe6d0;margin:0 auto 26px;display:flex;align-items:center;justify-content:center}
.benefit h3{font-size:18px;font-weight:700;margin-bottom:14px}
.benefit p{font-size:14px;line-height:22px;padding:0 30px}

/* testimonial */
.testi{position:absolute;top:3706px;left:0;width:1200px;height:530px}
.testi .quote{position:absolute;left:152px;top:80px;font-size:110px;line-height:1;font-weight:700;color:var(--navy)}
.testi h3{position:absolute;left:152px;top:160px;font-size:38px;font-weight:400;color:#111}
.testi p{position:absolute;left:152px;top:228px;width:530px;font-size:14px;line-height:26px;color:#444}
.testi .who{position:absolute;left:152px;top:362px;color:var(--green);font-size:17px;font-weight:600}
.stars{position:absolute;left:152px;top:392px;display:flex;gap:4px}
.stars span{width:26px;height:26px;background:var(--green);display:flex;align-items:center;justify-content:center}
.portrait{position:absolute;left:741px;top:89px;width:318px;height:318px;border-radius:50%;border:2px solid var(--navy-soft);padding:8px}
.portrait div{width:100%;height:100%;border-radius:50%;background:radial-gradient(circle at 50% 40%,#d9c2a8 0%,#4f8fc6 55%,#2f6fa8 100%)}
.arrow{position:absolute;top:240px;width:40px;height:40px;border-radius:50%;border:1px solid #ccc;display:flex;align-items:center;justify-content:center}

/* ready */
.ready h2{position:absolute;top:4300px;width:1200px;text-align:center;font-size:44px;font-weight:300;color:#111}
.ready .sub{position:absolute;top:4376px;width:1200px;text-align:center;font-size:17px;color:#222}
.ready h3{position:absolute;top:4448px;width:1200px;text-align:center;font-size:29px;font-weight:600;color:#111}
.ready .search{top:4516px;left:290px;width:624px}
.ready .call{top:4646px;left:560px}
.bins{position:absolute;top:4710px;left:0;width:1200px;height:126px;background:linear-gradient(180deg,rgba(17,26,61,0) 0%,rgba(17,26,61,.15) 60%,rgba(17,26,61,.35) 100%)}

/* footer */
.footer{position:absolute;top:4836px;left:0;width:1200px;height:458px;background:var(--navy);color:#fff}
.fcol{position:absolute;top:82px;font-size:14px}
.fcol h5{font-size:15px;font-weight:600;letter-spacing:.5px;margin-bottom:20px}
.fcol li{list-style:none;line-height:34px}
.fitem{display:flex;gap:10px;margin-bottom:24px;font-size:12px;line-height:18px}
.fitem b{font-size:14px;font-weight:600}
.email-box{width:290px;height:34px;background:#fff;color:#888;font-size:13px;display:flex;align-items:center;padding:0 10px;margin:18px 0 12px}
.send{width:128px;height:34px;background:var(--green);font-weight:700;display:flex;align-items:center;justify-content:center}
.frule{position:absolute;top:370px;left:110px;width:1000px;height:1px;background:#3b4570}
.copy{position:absolute;top:406px;width:1200px;text-align:center;font-size:13px}
</style>
</head>
<body>

<div class="topbar"><span>CALL NOW : 1800 555 014</span><div class="right"><span>Log in or Create account</span><span>🛒 Cart</span></div></div>
<header class="nav">
  <a class="brand" href="#"><span class="mark"></span>TUMBLE CRATE RENTALS OZ</a>
  <nav class="menu"><a>PRICING</a><a>LEARN MORE</a><a>ABOUT</a><a>TRADE SECRETS</a><a>CONTACT</a></nav>
  <div class="nav-rule" style="top:118px"></div>
</header>

<section class="hero">
  <div class="city" role="img" aria-label="Pale city skyline illustration"></div>
  <h1>1000's of Skips at Your Finger Tips</h1>
  <p class="tag">Best Service &amp; Price | Hassle Free | Australia Wide</p>
  <h2>Instant Quote</h2>
  <div class="search"><span>Enter Postcode or Suburb</span><span class="btn">Search</span></div>
  <a class="call">Call Now</a>
  <svg class="wave" width="1200" height="120" viewBox="0 0 1200 120"><path d="M0 60 Q300 130 600 70 T1200 40 V120 H0Z" fill="#fff"/></svg>
</section>

<div class="segments">
  <div class="seg" style="left:80px;top:0"><div class="c"><svg width="50" height="50" viewBox="0 0 24 24" fill="none" stroke="#222" stroke-width="1.6"><path d="M3 11 12 4l9 7"/><path d="M5 10v10h14V10"/><rect x="10" y="14" width="4" height="6"/></svg></div>Renovator</div>
  <div class="seg" style="left:295px;top:24px"><div class="c"><svg width="50" height="50" viewBox="0 0 24 24" fill="none" stroke="#222" stroke-width="1.6"><path d="M4 20 14 10M15 4l5 5-3 1-3-3zM4 4l16 16M4 4l3 0 0 3"/></svg></div>Tradie</div>
  <div class="seg active" style="left:520px;top:38px"><div class="c"><svg width="52" height="52" viewBox="0 0 24 24" fill="none" stroke="#fff" stroke-width="1.6"><rect x="4" y="6" width="16" height="13"/><path d="M4 10h16M9 6v13"/></svg></div>Builder</div>
  <div class="seg" style="left:745px;top:24px"><div class="c"><svg width="50" height="50" viewBox="0 0 24 24" fill="none" stroke="#222" stroke-width="1.6"><rect x="3" y="8" width="18" height="12" rx="1"/><path d="M9 8V5h6v3M3 13h18"/></svg></div>Corporate</div>
  <div class="seg" style="left:960px;top:0"><div class="c"><svg width="50" height="50" viewBox="0 0 24 24" fill="none" stroke="#222" stroke-width="1.6"><path d="M3 9l2-5h14l2 5zM4 9v11h16V9"/><rect x="9" y="13" width="6" height="7"/></svg></div>National</div>
</div>

<h2 class="section-title" style="top:955px">About Us</h2>
<p class="about-text">It is a long established fact that a reader will be distracted by the readable content of a page when looking at its layout. The point of using Lorem Ipsum is that it has a more-or-less normal distribution of letters, as opposed to using 'Content here, content here', making it look like readable English. Many desktop publishing packages and web page editors now use Lorem Ipsum as their default model text, and a search for 'lorem ipsum' will uncover many web sites still in their infancy.</p>

<div class="grey-band" style="top:1535px;height:730px"></div>
<div class="video" role="img" aria-label="Animated explainer video still: a cartoon homeowner beside a house asking where his skip bin is">
  <div class="play"><svg width="28" height="28" viewBox="0 0 24 24"><path d="M7 4l13 8-13 8z" fill="#2a2f5c"/></svg></div>
</div>

<h2 class="section-title" style="top:1795px">As Easy As 1, 2, 3...</h2>
<div class="step" style="left:152px">
  <svg width="60" height="48" viewBox="0 0 30 24" fill="var(--green)"><rect x="0" y="0" width="18" height="12" rx="2"/><rect x="10" y="8" width="18" height="12" rx="2"/></svg>
  <h3>Simple, Easy Booking</h3><p>Neque porro quisquam est qui dolorem ipsum</p></div>
<div class="step mid" style="left:463px">
  <svg width="62" height="50" viewBox="0 0 30 24" fill="none" stroke="#fff" stroke-width="1.8"><rect x="3" y="2" width="24" height="15" rx="1"/><path d="M1 21h28"/></svg>
  <h3>Instant Confirmation</h3><p>Neque porro quisquam est qui dolorem ipsum</p></div>
<div class="step" style="left:794px">
  <svg width="62" height="48" viewBox="0 0 30 24" fill="var(--green)"><path d="M2 6h26l-4 16H6z"/></svg>
  <h3>Gone When Your Ready!</h3><p>Neque porro quisquam est qui dolorem ipsum</p></div>

<h2 class="section-title" style="top:2300px">Trade Secrets</h2>
<article class="card" style="left:95px;width:597px">
  <div class="photo" role="img" aria-label="Photo of a smiling construction worker in a hard hat" style="background:linear-gradient(135deg,#c9a27a,#8a6a4f 50%,#e0b24a)"></div>
  <div class="body"><h4>14 Tips for Construction Tender Success</h4><p>Winning the next project is always a challenge. Get it right, and you've landed a nice job with good margin. Get it wrong though, and you can soon find yourself in hot water. After 12 years as a Builder, I've had my fair share of successes.</p><span class="more">READ MORE &gt;</span></div>
</article>
<article class="card" style="left:727px;width:378px">
  <div class="photo" role="img" aria-label="Photo of a couple holding a cardboard house cutout" style="background:linear-gradient(135deg,#e8e2da,#c59a6a 55%,#a07a52)"></div>
  <div class="body" style="text-align:center"><h4>Budget Renovation</h4><p>Renovating is a fantastic way to add value to your home or make it the home of your dreams.</p><span class="more">READ MORE &gt;</span></div>
</article>

<section class="save">
  <h2>Save Time. Save Money.</h2>
  <div class="benefit" style="left:90px"><div class="c"><svg width="80" height="80" viewBox="0 0 24 24" fill="none" stroke="#222" stroke-width="1.2"><path d="M12 21s-6-6-6-11a6 6 0 0 1 12 0c0 5-6 11-6 11z"/><circle cx="12" cy="10" r="2"/></svg></div><h3>Any Bin, Anytime, Anywhere</h3><p>It is a long established fact that a reader will be distracted by the readable content</p></div>
  <div class="benefit" style="left:450px"><div class="c"><svg width="80" height="80" viewBox="0 0 24 24" fill="none" stroke="#222" stroke-width="1.2"><circle cx="12" cy="9" r="4"/><path d="M4 21c1-4 4-6 8-6s7 2 8 6M7 9a5 5 0 0 1 10 0"/></svg></div><h3>Service Guaranteed</h3><p>It is a long established fact that a reader will be distracted by the readable content</p></div>
  <div class="benefit" style="left:810px"><div class="c"><svg width="80" height="80" viewBox="0 0 24 24" fill="none" stroke="#222" stroke-width="1.2"><rect x="3" y="7" width="18" height="11" rx="1"/><circle cx="12" cy="12.5" r="2.5"/></svg></div><h3>Best Pricing</h3><p>It is a long established fact that a reader will be distracted by the readable content</p></div>
</section>

<section class="testi">
  <div class="arrow" style="left:60px"><svg width="14" height="14" viewBox="0 0 24 24"><path d="M15 4 7 12l8 8" stroke="#555" stroke-width="2.5" fill="none"/></svg></div>
  <div class="arrow" style="left:1100px"><svg width="14" height="14" viewBox="0 0 24 24"><path d="M9 4l8 8-8 8" stroke="#555" stroke-width="2.5" fill="none"/></svg></div>
  <div class="quote">&ldquo;</div>
  <h3>Five Star Service</h3>
  <p>"It is a long established fact that a reader will be distracted by the readable content of a page when looking at its layout. The point of using Lorem Ipsum is that it has a more-or-less normal distribution of letters, as opposed to using 'Content here, content here', making it look like "</p>
  <div class="who">Alex Warden Cloud Engineer</div>
  <div class="stars"><span>★</span><span>★</span><span>★</span><span>★</span><span>★</span></div>
  <div class="stars" style="display:none"></div>
  <div class="portrait"><div role="img" aria-label="Portrait photo of the reviewer in a blue shirt"></div></div>
</section>
<style>.stars span{color:#fff;font-size:16px}</style>

<div class="grey-band" style="top:4236px;height:600px"></div>
<section class="ready">
  <h2>We're ready to go!</h2>
  <p class="sub">To book, ask questions or just for a chat, call us 7 days a week, 7.30am to 8pm</p>
  <h3>Quick Quote</h3>
  <div class="search"><span>Enter Postcode or Suburb</span><span class="btn">Search</span></div>
  <a class="call">Call Now</a>
</section>
<div class="bins" role="img" aria-label="Row of line-drawn skip bins along the ground with trees and birds"></div>

<footer class="footer">
  <div class="fcol" style="left:110px"><h5>CONTACT US</h5>
    <div class="fitem"><svg width="16" height="14" viewBox="0 0 24 18" fill="none" stroke="#fff" stroke-width="2"><rect x="1" y="1" width="22" height="16"/><path d="M1 1l11 9 11-9"/></svg><div><b>EMAIL ADDRESS</b><br>hello@tumblecrate.example.au</div></div>
    <div class="fitem"><svg width="16" height="16" viewBox="0 0 24 24" fill="none" stroke="#fff" stroke-width="2"><path d="M5 3h4l2 5-3 2a12 12 0 0 0 6 6l2-3 5 2v4a2 2 0 0 1-2 2A18 18 0 0 1 3 5a2 2 0 0 1 2-2z"/></svg><div><b>PHONE NUMBER</b><br>0400 555 927</div></div>
  </div>
  <div class="fcol" style="left:345px"><h5>AUSTRALIA WIDE</h5><ul><li>Sydney</li><li>Melbourne</li><li>Brisbane</li><li>Perth</li><li>Adelaide</li><li>Canberra</li></ul></div>
  <div class="fcol" style="left:582px"><h5>LEARN MORE</h5><ul><li>Waste Types</li><li>Skip Bin Sizes</li><li>Refund Policy</li><li>Pay Later with FlexiPay</li><li>FAQ</li><li>Privacy</li></ul></div>
  <div class="fcol" style="left:815px;width:300px"><h5>GET IN TOUCH</h5><p style="line-height:24px">Sign up for the latest news, offers from TUMBLE CRATE RENTALS OZ</p><div class="email-box">Email address</div><div class="send">SEND</div></div>
  <div class="frule"></div>
  <p class="copy">© Copyright 2019 . All Rights Reserved. Terms and Conditions</p>
</footer>

</body>
</html>
```